Crestline Lending Group Business Cards

We are looking to revamp the current business cards each of our locations uses. We are a lending company that specializes in personal loans, title loans, and tax services. We have locations in New Mexico, Texas, and Oklahoma.

We would like a cleaner, sleeker look while still highlighting what we offer. Title Loans, Personal Loans & Tax Services. We also want to include our referral fee somewhere on the card. We would like to see an English option as well as a Spanish option for the cards.

PLEASE NOTE: Some business cards do not include the employee's name but just the store's location, while others will include both.

These are double-sided business cards, and we would like to see proof if possible. I have included proofs of our current business cards for you to review below, as well as our company logo. Feel free to get creative with the logo, etc! Colors should match the logo; however, you do not need to use all of our logo colors if you don't want to.

```html
<!DOCTYPE html>
<html lang="en">
<head>
<meta charset="utf-8">
<title>Crestline Lending Group – Business Cards</title>
<link rel="stylesheet" href="https://fonts.googleapis.com/css2?family=Libre+Baskerville:wght@400;700&display=swap">
<style>
  :root {
    --stage: #58595b;
    --green: #134f30;
    --red: #c1232a;
    --white: #ffffff;
    --stripe: #f4f5f5;
    --serif: "Libre Baskerville", Georgia, serif;
  }
  * { margin: 0; padding: 0; box-sizing: border-box; }
  html, body { width: 1200px; height: 1200px; overflow: hidden; }
  body { background: var(--stage); position: relative; font-family: var(--serif); }

  .card {
    position: absolute;
    left: 197px;
    width: 806px;
    height: 461px;
    overflow: hidden;
    background:
      repeating-linear-gradient(90deg, var(--white) 0 14px, var(--stripe) 14px 28px);
    box-shadow: 4px 8px 14px rgba(0,0,0,.45);
  }
  .card--front { top: 120px; }
  .card--back  { top: 619px; }
  .card__shapes { position: absolute; inset: 0; width: 806px; height: 461px; }

  .brand-name {
    position: absolute;
    font-family: var(--serif);
    font-weight: 700;
    line-height: 1.1;
    letter-spacing: .5px;
    white-space: nowrap;
  }
  .card--front .brand-name { left: 30px; top: 85px; font-size: 46px; color: var(--green); }
  .card--back  .brand-name { left: 28px; top: 300px; font-size: 33px; color: var(--white); }

  .person {
    position: absolute; right: 28px; top: 44px; width: 250px;
    text-align: center; white-space: nowrap;
  }
  .person__name { font-size: 28px; font-weight: 700; color: var(--green); letter-spacing: .5px; line-height: 1; }
  .person__role { font-size: 18px; font-weight: 700; color: var(--red); letter-spacing: 1.2px; margin-top: 10px; }

  .contact-rail {
    position: absolute; left: 29px; top: 270px; width: 32px; height: 128px;
    background: var(--green); border-radius: 0 0 16px 16px;
  }
  .contact-icon { position: absolute; left: 8px; width: 16px; height: 16px; }
  .contact-list { position: absolute; left: 71px; top: 286px; list-style: none; color: var(--white); font-weight: 700; font-size: 20px; letter-spacing: 1.6px; white-space: nowrap; }
  .contact-list li { line-height: 1; margin-bottom: 14px; }
  .contact-list .contact-email { font-size: 18.5px; }
  .contact-list .address { line-height: 1.35; font-size: 19.5px; }

  .services { position: absolute; left: 535px; top: 306px; list-style: none; color: var(--white); font-weight: 700; font-size: 26px; line-height: 38px; white-space: nowrap; }
  .services li::before { content: "• "; font-size: 20px; }

  .referral { position: absolute; left: 420px; top: 148px; white-space: nowrap; }
  .referral__lead { font-size: 41px; font-weight: 700; color: var(--green); letter-spacing: -.5px; }
  .referral__get  { font-size: 58px; font-weight: 700; color: var(--red); margin-top: 4px; letter-spacing: -1px; line-height: 1.1; }
  .referral__amount { font-size: 124px; font-weight: 700; color: var(--red); line-height: 1; letter-spacing: -2px; }
</style>
</head>
<body>

<section class="card card--front" aria-label="Business card front">
  <svg class="card__shapes" viewBox="0 0 806 461" aria-hidden="true">
    <rect x="0" y="270" width="530" height="162" fill="var(--red)"/>
    <path d="M508,0 Q492,130 606,198 L618,192 Q514,128 518,0 Z" fill="var(--green)"/>
    <path d="M382,461 Q520,170 806,120 L806,461 Z" fill="var(--red)"/>
    <path d="M395,461 Q538,202 806,152 L806,461 Z" fill="var(--white)"/>
    <path d="M420,461 Q560,232 806,178 L806,461 Z" fill="var(--green)"/>
  </svg>

  <div class="brand-name">Crestline<br>Lending Group</div>

  <div class="person">
    <div class="person__name">JANE RIVERA</div>
    <div class="person__role">Branch Manager</div>
  </div>

  <div class="contact-rail">
    <svg class="contact-icon" style="top:18px" viewBox="0 0 16 16" aria-hidden="true"><path d="M3 1l3 3-2 2c1 2 3 4 5 5l2-2 3 3-2 3C6 15 1 10 1 3z" fill="var(--white)"/></svg>
    <svg class="contact-icon" style="top:56px" viewBox="0 0 16 16" aria-hidden="true"><rect x="1" y="4" width="14" height="9" fill="var(--white)"/><path d="M1 4l7 5 7-5" stroke="var(--green)" stroke-width="1.3" fill="none"/></svg>
    <svg class="contact-icon" style="top:88px" viewBox="0 0 16 16" aria-hidden="true"><path d="M8 1a5 5 0 0 1 5 5c0 4-5 9-5 9S3 10 3 6a5 5 0 0 1 5-5z" fill="var(--white)"/><circle cx="8" cy="6" r="2" fill="var(--green)"/></svg>
  </div>
  <ul class="contact-list">
    <li>(505) 555-0148</li>
    <li class="contact-email">hello@crestlinelending.com</li>
    <li class="address">456 Oak Avenue, Suite C,<br>Riverton, Texas 55501</li>
  </ul>

  <ul class="services">
    <li>Title Loans</li>
    <li>Personal Loans</li>
    <li>Tax Services</li>
  </ul>
</section>

<section class="card card--back" aria-label="Business card back">
  <svg class="card__shapes" viewBox="0 0 806 461" aria-hidden="true">
    <path d="M212,206 Q540,-10 806,138 L806,146 Q540,12 232,218 Z" fill="var(--green)"/>
    <path d="M0,122 Q335,150 412,461 L0,461 Z" fill="var(--red)"/>
    <path d="M0,153 Q312,175 398,461 L0,461 Z" fill="var(--white)"/>
    <path d="M0,178 Q300,200 385,461 L0,461 Z" fill="var(--green)"/>
  </svg>

  <div class="brand-name">Crestline<br>Lending Group</div>

  <div class="referral">
    <div class="referral__lead">Refer a Friend</div>
    <div class="referral__get">GET up tp</div>
    <div class="referral__amount">$100</div>
  </div>
</section>

</body>
</html>
```